VoltaRush Product Logo and Package

***Update*** Please you the text from the attached images on the product design.
Suggested Text:
Logo - VoltaRush
Title - Beta-hydroxybutyrates (BHB)Â Ketone Supplement
Beta-hydroxybutyrates (BHB)Â Ketone Supplement
Beta-hydroxybutyrates (BHB)Â Exogenous Ketones
Beta-hydroxybutyrates (BHB)Â Salts
Instant Ketones
3) Flavor - Orange Mango
4) Servings - 30 Servings 12g BHB Per Serving
5) Seals - Made in USA, FDA Certified Facility, GF (gluten Free), Dairy Free, Keto Friendly, Vegan Friendly, Non-GMO, Naturally Flavored, No Preservatives
6) Uses - Energy, Mental Clarity, Fat Loss, Muscle Strength, Appetite Suppression, Mood Management
7) Big Benefit - Formulated To Induce Rapid Ketosis.
Enjoy the benefits of Ketosis anytime!
50% More Servings Compared To Other Leading Brands!
I would like a logo and package designed for a supplement.
It is a powdered supplement that can be packaged in a plastic jar (8-16 oz) or a bag.
We will also be adding additional products to this line and would like the branding to scale.
The product is packaged in a 16 oz tub.
Product Title: Beta-hydroxybutyrates (BHB) Ketone Supplement
Brand Name: VoltaRush (I'd like the logo image to share the E)
Updates
Project Deadline Extended
Reason: I'd like to attract more designers and give them more time to submit briefs.
Target Market(s)
Health and Fitness Enthusiasts. Specifically those interested in a Ketogenic Lifestyle.
Industry/Entity Type
Health And Wellness
Requirements
Must have
- Modern, trendy, design.
- Bold colors and fonts.
- Professional but trendy.
- I would like to see Red and Black as the colors used.
Should not have
- Standard, corporate feel.
- Must be fun, engaging, and exciting.

```html
<!DOCTYPE html>
<html lang="en">
<head>
<meta charset="utf-8">
<title>VoltaRush BHB Ketone Supplement – Label</title>
<link rel="stylesheet" href="https://fonts.googleapis.com/css2?family=Bebas+Neue&family=Oswald:wght@400;500;600;700&family=Montserrat:wght@500;600;700&display=swap">
<style>
  :root {
    --bg: #ffffff;
    --label: #1d1b1c;
    --label-edge: #141213;
    --red: #e01b24;
    --white: #f4f4f4;
    --grey: #8c8c8c;
    --ribbon-tail: #6b6b6b;
    --green: #4caf3a;
    --orange: #ec8a2e;
    --facts-bg: #f2f2f2;
    --ink: #111111;
  }
  * { margin: 0; padding: 0; box-sizing: border-box; }
  html, body { width: 1200px; height: 1055px; overflow: hidden; background: var(--bg); }
  .canvas { position: relative; width: 1200px; height: 1055px; }

  .label {
    position: absolute; left: 20px; top: 168px; width: 1160px; height: 720px;
    background: var(--label); display: flex;
  }
  .panel { position: relative; height: 100%; }
  .panel-side { width: 300px; }
  .panel-front { width: 560px; border-left: 1px solid var(--label-edge); border-right: 1px solid var(--label-edge); }

  /* Front panel */
  .brand { position: absolute; top: 58px; left: 0; right: 0; display: flex; justify-content: center; align-items: center; gap: 12px; }
  .brand-dot { width: 16px; height: 16px; border-radius: 50%; background: var(--red); }
  .brand-name { font-family: "Montserrat", sans-serif; font-weight: 600; font-size: 40px; color: var(--white); }

  .title-row { position: absolute; top: 112px; left: 0; right: 0; display: flex; justify-content: center; align-items: center; gap: 22px; }
  .title-arrow { width: 0; height: 0; border-top: 22px solid transparent; border-bottom: 22px solid transparent; }
  .title-arrow.left { border-right: 30px solid var(--white); }
  .title-arrow.right { border-left: 30px solid var(--white); }
  .title-bhb { font-family: "Bebas Neue", sans-serif; font-size: 140px; line-height: 1; color: var(--red); letter-spacing: 2px; }

  .subtitle { position: absolute; top: 240px; left: 0; right: 0; text-align: center; font-family: "Bebas Neue", sans-serif; font-size: 44px; color: var(--white); letter-spacing: 0.5px; }

  .ribbon { position: absolute; top: 292px; left: 0; right: 0; height: 60px; }
  .ribbon svg { position: absolute; inset: 0; }
  .ribbon-text { position: absolute; left: 90px; right: 90px; top: 6px; height: 44px; background: var(--red); border: 2px solid var(--white); display: flex; align-items: center; justify-content: center; font-family: "Oswald", sans-serif; font-weight: 700; font-size: 30px; letter-spacing: 4px; color: var(--white); }

  .benefits { position: absolute; top: 360px; left: 0; width: 560px; height: 220px; }
  .benefits svg { position: absolute; inset: 0; }
  .benefit { position: absolute; font-family: "Bebas Neue", sans-serif; color: var(--white); line-height: 1; }
  .benefit .big { font-size: 27px; }
  .benefit .small { font-size: 19px; }
  .benefit-fuel { top: 38px; left: 0; right: 0; text-align: center; font-size: 22px; }
  .benefit-fat { top: 96px; left: 98px; font-size: 23px; }
  .benefit-appetite { top: 96px; left: 382px; font-size: 23px; }
  .benefit-weight { top: 166px; left: 0; right: 0; text-align: center; }
  .benefit-weight .small { font-size: 15px; display: block; margin-bottom: 4px; }
  .benefit-weight .big { font-size: 28px; }

  .flavour { position: absolute; top: 590px; left: 50%; transform: translateX(-50%); background: var(--orange); padding: 2px 10px; font-family: "Bebas Neue", sans-serif; font-size: 28px; color: var(--white); letter-spacing: 0.5px; }
  .servings { position: absolute; top: 628px; left: 0; right: 0; text-align: center; font-family: "Montserrat", sans-serif; color: var(--white); }
  .servings-count { display: inline-block; font-weight: 700; font-size: 24px; letter-spacing: 1px; padding-bottom: 2px; border-bottom: 2px dashed var(--green); }
  .servings-dose { display: block; font-weight: 700; font-size: 14px; letter-spacing: 0.8px; margin-top: 2px; }

  .front-foot { position: absolute; top: 690px; font-family: "Oswald", sans-serif; font-weight: 500; font-size: 14px; color: var(--white); }
  .front-foot.left { left: 40px; }
  .front-foot.right { right: 40px; }

  /* Left panel */
  .seals { position: absolute; top: 110px; left: 70px; display: grid; grid-template-columns: repeat(2, 70px); gap: 18px 26px; }
  .seal { width: 70px; height: 70px; border-radius: 50%; border: 3px solid var(--grey); background: var(--label); }
  .divider { position: absolute; left: 40px; right: 40px; border-top: 2px dashed var(--green); }
  .uses { position: absolute; left: 50px; right: 40px; list-style: none; font-family: "Oswald", sans-serif; font-weight: 400; font-size: 16px; color: var(--white); }
  .uses li { height: 36px; display: flex; align-items: center; gap: 10px; }
  .uses li::before { content: ""; width: 8px; height: 8px; border-radius: 50%; background: var(--red); }
  .anytime { position: absolute; top: 575px; left: 24px; right: 24px; height: 58px; background: var(--red); border: 2px solid var(--white); display: flex; align-items: center; justify-content: center; text-align: center; font-family: "Bebas Neue", sans-serif; font-size: 24px; line-height: 1; color: var(--white); padding: 0 10px; }

  /* Right panel */
  .more-servings { position: absolute; top: 100px; left: 40px; right: 40px; background: var(--red); color: var(--white); font-family: "Bebas Neue", sans-serif; display: flex; align-items: center; gap: 10px; padding: 6px 12px; }
  .more-servings .pct { font-size: 52px; line-height: 1; }
  .more-servings .note { font-size: 17px; line-height: 1.05; }
  .facts { position: absolute; top: 190px; left: 40px; right: 40px; background: var(--facts-bg); color: var(--ink); border: 2px solid var(--ink); padding: 6px 8px; font-family: "Oswald", sans-serif; font-size: 12px; line-height: 1.35; }
  .facts-title { font-weight: 700; font-size: 22px; line-height: 1.1; border-bottom: 1px solid var(--ink); padding-bottom: 2px; }
  .facts-row { display: flex; justify-content: space-between; border-bottom: 1px solid var(--ink); padding: 1px 0; }
  .facts-row.thick { border-bottom-width: 5px; }
  .facts-row.head { font-weight: 700; }
  .facts-note { font-size: 11px; padding-top: 3px; }
  .facts-other { font-size: 11px; padding-top: 4px; border-top: 3px solid var(--ink); margin-top: 3px; }
  .made-for { position: absolute; top: 520px; left: 40px; font-family: "Oswald", sans-serif; font-size: 13px; color: var(--grey); }
</style>
</head>
<body>
<div class="canvas">
  <div class="label">

    <section class="panel panel-side panel-left">
      <div class="seals">
        <div class="seal"></div><div class="seal"></div>
        <div class="seal"></div><div class="seal"></div>
      </div>
      <div class="divider" style="top:300px"></div>
      <ul class="uses" style="top:312px">
        <li>Energy</li>
        <li>Mental Clarity</li>
        <li>Fat Loss</li>
        <li>Muscle Strength</li>
        <li>Appetite Suppression</li>
        <li>Mood Management</li>
      </ul>
      <div class="divider" style="top:540px"></div>
      <div class="anytime">Enjoy the benefits of Ketosis anytime!</div>
    </section>

    <section class="panel panel-front">
      <div class="brand">
        <span class="brand-dot"></span>
        <span class="brand-name">VoltaRush</span>
      </div>

      <div class="title-row">
        <span class="title-arrow left"></span>
        <span class="title-bhb">BHB</span>
        <span class="title-arrow right"></span>
      </div>
      <div class="subtitle">Beta Hydroxybutyrates</div>

      <div class="ribbon">
        <svg width="560" height="60" viewBox="0 0 560 60">
          <polygon points="60,18 100,18 100,58 60,58 72,38" fill="var(--ribbon-tail)"/>
          <polygon points="500,18 460,18 460,58 500,58 488,38" fill="var(--ribbon-tail)"/>
        </svg>
        <div class="ribbon-text">KETONE SUPPLEMENT</div>
      </div>

      <div class="benefits">
        <svg width="560" height="220" viewBox="0 0 560 220">
          <line x1="40" y1="50" x2="520" y2="200" stroke="var(--green)" stroke-width="2" stroke-dasharray="9 6"/>
          <line x1="520" y1="50" x2="40" y2="200" stroke="var(--green)" stroke-width="2" stroke-dasharray="9 6"/>
          <circle cx="40" cy="50" r="3" fill="var(--green)"/>
          <circle cx="520" cy="50" r="3" fill="var(--green)"/>
          <circle cx="40" cy="200" r="3" fill="var(--green)"/>
          <circle cx="520" cy="200" r="3" fill="var(--green)"/>
          <circle cx="280" cy="16" r="20" fill="none" stroke="var(--red)" stroke-width="4"/>
          <circle cx="280" cy="16" r="7" fill="var(--red)"/>
          <circle cx="280" cy="148" r="20" fill="none" stroke="var(--red)" stroke-width="4"/>
          <circle cx="280" cy="148" r="7" fill="var(--red)"/>
          <circle cx="72" cy="122" r="16" fill="var(--red)"/>
          <circle cx="490" cy="122" r="16" fill="var(--red)"/>
        </svg>
        <div class="benefit benefit-fuel"><span class="big">2X</span> MORE FUEL THAN<br>CARBS &amp; PROTEIN</div>
        <div class="benefit benefit-fat">LOSE FAT<br>WITH FAT</div>
        <div class="benefit benefit-appetite">APPETITE<br>CONTROL</div>
        <div class="benefit benefit-weight"><span class="small">ENHANCED THERMOGENIC</span><span class="big">WEIGHT LOSS</span></div>
      </div>

      <div class="flavour">ORANGE FLAVOUR</div>
      <div class="servings">
        <span class="servings-count">30 SERVINGS</span>
        <span class="servings-dose">12g BHB PER SERVING</span>
      </div>

      <div class="front-foot left">DIETARY SUPPLEMENT</div>
      <div class="front-foot right">NET WEIGHT 16 OZ (454G)</div>
    </section>

    <section class="panel panel-side panel-right">
      <div class="more-servings">
        <span class="pct">50%</span>
        <span class="note">More servings compared to other leading brands!</span>
      </div>
      <div class="facts">
        <div class="facts-title">Supplement Facts</div>
        <div>Serving Size 1 Scoop</div>
        <div class="facts-row thick"><span>Servings Per Container 30</span></div>
        <div class="facts-row head"><span>Amount Per Serving</span><span>% DV</span></div>
        <div class="facts-row head"><span>BHB Blend</span><span>12g</span></div>
        <div class="facts-row"><span>Calcium BHB</span><span>4g</span></div>
        <div class="facts-row"><span>Sodium BHB</span><span>4g</span></div>
        <div class="facts-row"><span>Magnesium BHB</span><span>4g</span></div>
        <div class="facts-note">Daily Value not established</div>
        <div class="facts-other">Other ingredients: citric acid, natural orange flavor, stevia.</div>
      </div>
      <div class="made-for">Manufactured for VoltaRush</div>
    </section>

  </div>
</div>
</body>
</html>
```